letter head for a construction company

Company Name: Zaviro Construction Limited

Address: Kilele Street, Tengeru Shores, Dar es salaam, Tanzania

Phone: 0754382916

email : info@zaviroconstruction.example

website : www.zaviroconstruction.example

```html
<!DOCTYPE html>
<html lang="en">
<head>
<meta charset="utf-8">
<title>Zaviro Construction Limited – Letterhead</title>
<link rel="stylesheet" href="https://fonts.googleapis.com/css2?family=Source+Sans+3:wght@400;600;700&display=swap">
<style>
  :root {
    --backdrop: #f0f1f0;
    --paper: #ffffff;
    --ink: #3d3d3d;
    --ink-soft: #4a4a4a;
    --accent: #ee7a12;
    --rule: #3c3c3c;
  }
  * { margin: 0; padding: 0; box-sizing: border-box; }
  html, body {
    width: 1052px; height: 1200px; overflow: hidden;
    background: var(--backdrop);
    font-family: "Source Sans 3", "Myriad Pro", sans-serif;
    color: var(--ink);
  }
  .letterhead {
    position: absolute; left: 244px; top: 201px;
    width: 565px; height: 800px;
    background: var(--paper);
  }
  .frame { position: absolute; inset: 0; width: 565px; height: 800px; }
  .brand {
    position: absolute; top: 52px; left: 0; width: 100%;
    display: flex; justify-content: center; align-items: center; gap: 7px;
  }
  .brand-mark { width: 10px; height: 10px; background: var(--accent); }
  .brand-name {
    font-size: 20px; font-weight: 700; color: var(--ink);
    letter-spacing: 0.2px;
  }
  .letter-body {
    position: absolute; left: 24px; top: 177px; width: 512px;
    font-size: 10.6px; line-height: 15.6px; color: var(--ink-soft);
  }
  .salutation { color: var(--accent); font-weight: 700; margin-bottom: 9px; }
  .letter-body p.para { margin-bottom: 19px; }
  .sign-off { position: absolute; left: 24px; top: 529px; width: 72px; }
  .sign-from { font-size: 10.5px; color: var(--accent); line-height: 12px; }
  .sign-company { font-size: 8.6px; font-weight: 700; color: var(--ink); line-height: 11px; white-space: nowrap; }
  .signature {
    margin-top: 8px; width: 70px; height: 27px;
    background: linear-gradient(90deg, #f4f4f4, #e6e6e6 50%, #f4f4f4);
  }
  .signature-line { border-top: 0.8px solid var(--rule); }
  .signature-label {
    font-size: 4.6px; color: var(--accent); text-align: center;
    letter-spacing: 0.2px; margin-top: 3px;
  }
  .contact {
    position: absolute; left: 0; top: 694px; width: 100%;
    text-align: center; font-size: 10.6px; line-height: 15.8px; color: var(--ink-soft);
    list-style: none;
  }
  .contact strong { font-weight: 700; color: var(--ink); }
</style>
</head>
<body>
  <main class="letterhead">
    <svg class="frame" viewBox="0 0 537 760" aria-hidden="true">
      <polyline points="0,22 512,22 463,92 537,92" fill="none" stroke="var(--rule)" stroke-width="2.2"/>
      <polygon points="537,0 537,86 479,86" fill="var(--accent)"/>
      <polyline points="0,658 53,735 537,735" fill="none" stroke="var(--rule)" stroke-width="2.2"/>
      <polygon points="0,674 0,760 57,760" fill="var(--accent)"/>
    </svg>

    <header class="brand">
      <span class="brand-mark"></span>
      <span class="brand-name">Zaviro Construction Limited</span>
    </header>

    <section class="letter-body">
      <p class="salutation">Dear Client,</p>
      <p class="para">Lorem Ipsum is simply dummy text of the printing and typesetting industry. Lorem Ipsum has been the industry's standard dummy text ever since the 1500s, when an unknown printer took a galley of type and scrambled it to make a type specimen book. It has survived not only five centuries, but also the leap into electronic typesetting, remaining essentially unchanged. It was popularised in the 1960s with the release of Lettrafold sheets containing Lorem Ipsum passages, and more recently with desktop publishing software like Pagewright Studio including versions of Lorem Ipsum.</p>
      <p class="para">Lorem Ipsum is simply dummy text of the printing and typesetting industry. Lorem Ipsum has been the industry's standard dummy text ever since the 1500s, when an unknown printer took a galley of type and scrambled</p>
      <p class="para">Lorem Ipsum is simply dummy text of the printing and typesetting industry. Lorem Ipsum has been the industry's standard dummy text ever since the 1500s, when an unknown printer took a galley of type and scrambled it to make a type specimen book. It has survived not only five centuries, but also the leap into electronic typesetting, remaining essentially unchanged. It was popularised in the 1960s with the release of Lettrafold sheets containing Lorem Ipsum passages, and more recently with desktop publishing software like Pagewright Studio including versions of Lorem Ipsum.</p>
    </section>

    <section class="sign-off">
      <p class="sign-from">From</p>
      <p class="sign-company">Zaviro Construction Limited</p>
      <div class="signature" role="img" aria-label="Handwritten signature of the sender"></div>
      <div class="signature-line"></div>
      <p class="signature-label">SIGNATURE</p>
    </section>

    <ul class="contact">
      <li><strong>Address:</strong> Kilele Street, Tengeru Shores, Dar es salaam, Tanzania</li>
      <li><strong>Phone:</strong> 0754382916</li>
      <li><strong>email:</strong> info@zaviroconstruction.example</li>
      <li><strong>website:</strong> www.zaviroconstruction.example</li>
    </ul>
  </main>
</body>
</html>
```